KESTREL REFRIGERATION Business Card design

We are looking for a business card design front and back. We would like our logo only on the front with all other details on the rear.
Rear should include name, email address and two phone numbers. Similar to the attachment.
Smart and bright.
Looking for a matt finish on all of the card but the logo to be gloss and slightly proud.

Contact Information for Business Card

Name - Gavin Holloway
Director
Phone - 0867302948
0417259083
email - gavin@kestrelrefrigeration.com.au
website - kestrelrefrigeration.com.au

Font styles to use
Serif

Requirements
Must have
• Colours from our logo. icons for phone, email etc.

```html
<!DOCTYPE html>
<html lang="en">
<head>
<meta charset="utf-8">
<title>Kestrel Refrigeration – Business Card</title>
<link rel="stylesheet" href="https://fonts.googleapis.com/css2?family=Arimo:wght@400;700&display=swap">
<style>
  :root {
    --backdrop: #232323;
    --card: #ecece9;
    --lime: #a9d466;
    --purple: #46296e;
    --ink: #2b2b2b;
  }
  * { box-sizing: border-box; margin: 0; padding: 0; }
  html, body { width: 1189px; height: 1200px; overflow: hidden; }
  body {
    background: var(--backdrop);
    font-family: "Arimo", Arial, sans-serif;
    position: relative;
  }
  .card {
    position: absolute;
    left: 166px;
    width: 856px;
    height: 489px;
    background: var(--card);
    box-shadow: 0 6px 18px rgba(0,0,0,0.45);
  }
  .card--front { top: 76px; }
  .card--back { top: 635px; }

  .wordmark {
    position: absolute;
    display: flex;
    flex-direction: column;
    align-items: center;
    color: var(--purple);
    font-weight: 700;
    line-height: 1;
  }
  .wordmark__dot {
    width: 26px; height: 26px; border-radius: 50%;
    background: var(--lime);
    margin-bottom: 18px;
  }
  .wordmark__primary { letter-spacing: 2px; }
  .wordmark__secondary { letter-spacing: 1px; }

  .card--front .wordmark { left: 0; right: 0; top: 150px; }
  .card--front .wordmark__primary { font-size: 92px; }
  .card--front .wordmark__secondary { font-size: 33px; margin-top: 22px; }

  .card--back .wordmark { left: 60px; width: 360px; top: 168px; }
  .card--back .wordmark__primary { font-size: 70px; }
  .card--back .wordmark__secondary { font-size: 26px; margin-top: 18px; }

  .divider {
    position: absolute;
    left: 430px; top: 154px;
    width: 1.5px; height: 180px;
    background: var(--purple);
  }
  .contact {
    position: absolute;
    left: 471px; top: 156px;
  }
  .contact__name { font-size: 29px; font-weight: 700; color: var(--ink); line-height: 1.1; }
  .contact__role { font-size: 20px; color: var(--purple); line-height: 1.1; margin-bottom: 26px; }
  .contact__list { list-style: none; }
  .contact__item {
    display: flex; align-items: center;
    font-size: 18.5px; color: var(--ink);
    height: 27.5px;
  }
  .contact__icon { width: 18px; height: 18px; margin-right: 17px; flex-shrink: 0; }
</style>
</head>
<body>
  <section class="card card--front" aria-label="Card front">
    <div class="wordmark">
      <span class="wordmark__dot"></span>
      <span class="wordmark__primary">KESTREL</span>
      <span class="wordmark__secondary">REFRIGERATION</span>
    </div>
  </section>

  <section class="card card--back" aria-label="Card back">
    <div class="wordmark">
      <span class="wordmark__dot"></span>
      <span class="wordmark__primary">KESTREL</span>
      <span class="wordmark__secondary">REFRIGERATION</span>
    </div>
    <div class="divider"></div>
    <div class="contact">
      <p class="contact__name">Gavin Holloway</p>
      <p class="contact__role">Director</p>
      <ul class="contact__list">
        <li class="contact__item">
          <svg class="contact__icon" viewBox="0 0 24 24"><path fill="#46296e" d="M6.6 2.5l3 .4 1 5-2.3 1.3c.9 2.6 2.6 4.9 4.6 6.4l2-1.7 4.6 2.2-.3 3.1c-.2 1.3-1.5 2.2-2.8 1.9C9 19.6 3.9 13.3 3.8 5.6 3.8 3.9 5 2.4 6.6 2.5z"/></svg>
          0867302948
        </li>
        <li class="contact__item">
          <svg class="contact__icon" viewBox="0 0 24 24"><path fill="#46296e" d="M6.6 2.5l3 .4 1 5-2.3 1.3c.9 2.6 2.6 4.9 4.6 6.4l2-1.7 4.6 2.2-.3 3.1c-.2 1.3-1.5 2.2-2.8 1.9C9 19.6 3.9 13.3 3.8 5.6 3.8 3.9 5 2.4 6.6 2.5z"/></svg>
          0417259083
        </li>
        <li class="contact__item">
          <svg class="contact__icon" viewBox="0 0 24 24"><rect x="2" y="5" width="20" height="14" fill="#46296e"/><path d="M2 5l10 8 10-8M2 19l7-7M22 19l-7-7" stroke="#ecece9" stroke-width="1.5" fill="none"/></svg>
          gavin@kestrelrefrigeration.com.au
        </li>
        <li class="contact__item">
          <svg class="contact__icon" viewBox="0 0 24 24" fill="none" stroke="#46296e" stroke-width="1.6"><circle cx="12" cy="12" r="9.5"/><ellipse cx="12" cy="12" rx="4" ry="9.5"/><path d="M2.5 12h19M4 7h16M4 17h16"/></svg>
          kestrelrefrigeration.com.au
        </li>
      </ul>
    </div>
  </section>
</body>
</html>
```